Buch-/E-Book-Cover für religiöse Texte
Zielgruppe
Wir schreiben Bücher für alle Zielgruppen. Der Ursprung ist die Bibel.
Aufgabenstellung
Die Texte haben sind biblisch religiös. Das Cover soll aber nicht unbedingt religiöse Symbole erhalten, da wir es nicht auf eine spezielle Käufergruppe ausrichten wollen. Das Motto -Ein Bild sagt mehr als Tausend Worte.
Titel des Buches: Das Licht über dem Tal
Unsere Vorstellung ist: Die Erde ist groß abgebildet, dahinter liegt eine Alte Bibel die von der Erdkugel überdeckt wird (ich lege ein PDF Bild bei). Auf der Erdkugel sollen die Probleme mit kleinen Symbolen sichtbar sein (Feuer, Bomben, Krieg, Korruption usw.)
Da die Texte aus dem Fundus von Kessing sind sollte die Klovano Figur von Kessing auf dem Cover sein, dezent aber nicht aufdringlich. Ein Bild der Figur und die Rechte zur Veröffentlichung habe ich bereits eingeholt. Die Bibelseite ist mein Eigentum. Der Titel des Buches lautet etwa. Gibt es einen Morgen?
Letztendlich ist das Ziel die Seligkeit.
Das alles sind unsere Vorstellungen: Neues oder Anderes ist willkommen.

```html
<!DOCTYPE html>
<html lang="de">
<head>
<meta charset="utf-8">
<title>Das Licht über dem Tal – Buchcover</title>
<link href="https://fonts.googleapis.com/css2?family=Arimo:wght@400;700&family=UnifrakturMaguntia&display=swap" rel="stylesheet">
<style>
  :root {
    --page: #f1f0ed;
    --page-ink: #2a2a2a;
    --rule: #555555;
    --ink: #111111;
    --paper: #ffffff;
    --globe-light: #dcdcdc;
    --globe-dark: #363636;
    --figure-tone: #6b6b6b;
  }
  html, body {
    margin: 0;
    padding: 0;
    overflow: hidden;
    background: var(--paper);
  }
  .cover {
    width: 771px;
    height: 1200px;
    position: relative;
    overflow: hidden;
    background: var(--page);
  }

  /* old bible page, set as real blackletter text */
  .bible-page {
    position: absolute;
    inset: 0;
    font-family: "UnifrakturMaguntia", serif;
    color: var(--page-ink);
  }
  .page-column {
    position: absolute;
    top: 0;
    height: 1200px;
    overflow: hidden;
    text-align: justify;
    hyphens: auto;
  }
  .column-left { left: 0; width: 298px; }
  .column-middle { left: 314px; width: 334px; }
  .column-right { left: 664px; width: 150px; }
  .column-rule {
    position: absolute;
    top: 0;
    width: 1px;
    height: 1200px;
    background: var(--rule);
  }
  .chapter-head {
    margin: 2px 0 4px 60px;
    font-size: 24px;
    line-height: 26px;
  }
  .verse {
    margin: 0;
    font-size: 22px;
    line-height: 24px;
  }
  .gloss {
    margin: 0 0 2px;
    font-size: 14.5px;
    line-height: 17px;
    padding-left: 6px;
  }

  .cover-art {
    position: absolute;
    inset: 0;
    display: block;
    width: 771px;
    height: 1200px;
  }
  .title-small,
  .title-large,
  .author-name {
    font-family: "Arimo", Arial, sans-serif;
    fill: var(--paper);
    stroke: var(--ink);
    paint-order: stroke fill;
  }
  .title-small { font-size: 38px; stroke-width: 3px; font-weight: 700; }
  .title-large { font-size: 176px; stroke-width: 4px; font-weight: 400; }
  .author-name { font-size: 17px; stroke-width: 1.2px; font-weight: 700; }
</style>
</head>
<body>
<main class="cover">
  <div class="bible-page" aria-hidden="true">
    <div class="page-column column-left">
      <p class="chapter-head">Das I. Capitel.</p>
      <p class="gloss">Gott hat innerhalb sechs Tagen Himel und Erden erschaffen, sampt allem, was darinnen beschlossen ist. II. Sonderlich aber hat er den Menschen zu seinem Ebenbild gemacht.</p>
      <p class="verse">Am Anfang schuff Gott Himel und Erde.</p>
      <p class="gloss">Anfang] Das ist: Da noch keine Zeit noch Materie war, und nichts denn Gott allein. Schuff Gott] Da ist er aus seiner Ewigkeit herfür getreten, und hat alles aus Nichts gemacht, mit Weisheit und Güte.</p>
      <p class="verse">Und die Erde war wüst und leer, und es war finster auff der Tieffe, und der Geist Gottes schwebet auff dem Wasser.</p>
      <p class="gloss">Wüst und leer] Das ist: Ungestaltet, ohne Hügel und Wälder, ohne Thier und Gewächs. Finster] Denn das Licht war noch nicht erschaffen, und alles lag in Nacht.</p>
      <p class="verse">Und Gott sprach: Es werde Liecht, und es ward Liecht.</p>
      <p class="gloss">Sprach] Diß Wort, dadurch Gott alle Ding erschaffen hat, ist der Sohn Gottes, durch den die Welt gemacht ist, und der Geist schwebet darüber. Welches Geheimniß hernach völlig offenbaret ward.</p>
      <p class="verse">Und Gott sahe, daß das Liecht gut war. Da scheidet Gott das Liecht vom Finsterniß.</p>
      <p class="gloss">Scheidet] Also, daß er eine besondere Zeit zur Arbeit und eine zur Ruhe gab, und alle Creaturen darnach geordnet wurden.</p>
      <p class="verse">Und nennet das Liecht Tag, und die Finsterniß Nacht. Da ward aus Abend und Morgen der erste Tag.</p>
      <p class="gloss">Erste Tag] Das ist: Dieser ist unter allen der erste Tag gewesen, und von ihm zählet man die andern Tage.</p>
    </div>
    <div class="column-rule" style="left:306px"></div>
    <div class="page-column column-middle">
      <p class="verse">Und Gott sprach: Es werde eine Veste zwischen den Wassern, und die sey ein Unterscheid zwischen den Wassern.</p>
      <p class="gloss">Sprach] Nemlich, am andern Tage, da Gott in dem angefangenen Werck der Schöpffung weiter fortgeschritten. Veste] Nemlich, ein runde Außbreitung oder Außdehnung des Himmels, an dem hernach am vierdten Tage die Sterne gesetzet worden.</p>
      <p class="verse">Da machet Gott die Veste, und scheidet das Wasser unter der Vesten von dem Wasser über der Vesten, und es geschach also.</p>
      <p class="gloss">Veste] Das ist der Himmel, in der mitte zwischen der Erde und den Wassern oben, darinnen die Lufft und die Wolcken gehen und ihren Lauff haben.</p>
      <p class="verse">Und Gott nennet die Vesten Himmel. Da ward aus Abend und Morgen der ander Tag.</p>
      <p class="gloss">Himmel] Nemlich den untern Himmel, darinnen die Vögel fliegen und der Regen fällt, welches ein grosses Wunder ist.</p>
      <p class="verse">Und Gott sprach: Es samle sich das Wasser unter dem Himmel an sonderliche Örter, daß man das Trocken sehe. Und es geschach also.</p>
      <p class="gloss">Samle] Denn zuvor war das Wasser so hienieden bliebe, noch mit der Erden auff einen Hauffen durch einander vermischet, biß Gott es schied.</p>
      <p class="verse">Und Gott nennet das Trocken Erde, und die Samlung der Wasser nennet er Meer, und Gott sahe, daß es gut war.</p>
      <p class="verse">Und Gott sprach: Es lasse die Erde auffgehen Graß und Kraut, das sich besame, und fruchtbare Bäume, da ein jeglicher nach seiner Art Frucht trage, und habe seinen eigen Samen bey ihm selbs auff Erden. Und es geschach also.</p>
      <p class="gloss">Das ist: Die Erde soll mancherley Kräuter und Bäume tragen, nicht allein die da wachsen, sondern auch die hernach, zu Nahrung und Speise der Menschen.</p>
    </div>
    <div class="column-rule" style="left:656px"></div>
    <div class="page-column column-right">
      <p class="gloss">der Artzney gebrauchen, mancherley Farben und einer jeden Art.</p>
      <p class="verse">Und die Erde ließ auffgehen Graß und Kraut, das sich besamete ein jegliches nach seiner Art, und Bäume die da Frucht trugen.</p>
      <p class="gloss">Bey sich selbst] Das ist: Daß er sich von ihm selbst besamen kan.</p>
      <p class="verse">Da ward aus Abend und Morgen der dritte Tag.</p>
      <p class="verse">Und Gott sprach: Es werden Liechter an der Veste des Himmels, und scheiden Tag und Nacht, und geben Zeichen, Zeiten, Tage und Jahre.</p>
      <p class="gloss">Liechter] Durch die Liechter verstehet man Sonne, Mond und Sterne, so den Tag und die Nacht regieren, und die Zeiten ordnen.</p>
      <p class="verse">Und seyen Liechter an der Veste des Himmels, daß sie scheinen auff Erden.</p>
      <p class="verse">Und Gott machte zwey grosse Liechter, ein groß Liecht und ein klein Liecht.</p>
    </div>
  </div>

  <svg class="cover-art" viewBox="0 0 771 1200" xmlns="http://www.w3.org/2000/svg">
    <defs>
      <radialGradient id="globeTone" cx="0.42" cy="0.36" r="0.72">
        <stop offset="0" stop-color="var(--globe-light)"/>
        <stop offset="0.55" stop-color="#8c8c8c"/>
        <stop offset="1" stop-color="var(--globe-dark)"/>
      </radialGradient>
    </defs>

    <!-- globe frame and globe -->
    <circle class="globe-frame" cx="397" cy="455" r="235" fill="var(--paper)" fill-opacity="0.55" stroke="var(--ink)" stroke-width="2"/>
    <circle class="globe" role="img" aria-label="Schwarzweiße Aufnahme der Erdkugel mit Wolken"
            cx="397" cy="455" r="217" fill="url(#globeTone)"/>

    <!-- problem symbols -->
    <g class="problem-icon">
      <circle cx="263" cy="190" r="42" fill="var(--paper)" fill-opacity="0.55" stroke="var(--ink)" stroke-width="2"/>
      <path role="img" aria-label="Feuer-Symbol" fill="var(--ink)"
            d="M263 160 C276 178 288 188 285 208 C283 222 272 230 263 230 C252 230 241 222 241 207 C241 195 249 188 252 178 C256 188 258 193 262 195 C265 185 265 172 263 160 Z"/>
    </g>
    <g class="problem-icon">
      <circle cx="402" cy="148" r="42" fill="var(--paper)" fill-opacity="0.55" stroke="var(--ink)" stroke-width="2"/>
      <path role="img" aria-label="Waffen-Symbol" fill="var(--ink)"
            d="M365 136 H436 V150 H402 L396 156 H390 L384 176 H368 L376 150 H365 Z"/>
    </g>
    <g class="problem-icon">
      <circle cx="542" cy="190" r="42" fill="var(--paper)" fill-opacity="0.55" stroke="var(--ink)" stroke-width="2"/>
      <path role="img" aria-label="Geldsack-Symbol" fill="var(--ink)"
            d="M530 160 H554 L547 175 C565 183 572 200 570 212 C568 224 558 228 542 228 C526 228 516 224 514 212 C512 200 519 183 537 175 Z"/>
      <text x="542" y="217" text-anchor="middle" font-family="Arimo, Arial, sans-serif" font-weight="700" font-size="28" fill="var(--paper)">$</text>
    </g>

    <!-- figure -->
    <circle class="kessing-figure" role="img" aria-label="Klovano-Figur von Kessing mit Buch"
            cx="390" cy="810" r="54" fill="var(--figure-tone)"/>

    <!-- title -->
    <text class="title-small" x="400" y="946" text-anchor="middle" textLength="345" lengthAdjust="spacingAndGlyphs">DAS LICHT ÜBER DEM</text>
    <text class="title-large" x="400" y="1104" text-anchor="middle" textLength="535" lengthAdjust="spacingAndGlyphs">TAL</text>
    <text class="author-name" x="398" y="1148" text-anchor="middle">AUTOR NAME</text>
  </svg>
</main>
</body>
</html>
```